Verbena Home- Hang tags for Modern Handmade Home Decor products

We need to design some hang tags to use for our products, we want double tags, meaning two tags that go together on one string, two different and coordinating sizes and shapes. We have a logo, what we need is the artwork for these two tags to take to print. One tag will have the logo on one side and company information on the other, the second tag will be for product information. For example, we specialize in handmade pieces from Latin America, on the product tag I want space to write the product info but also a line for what country it's from and what community created it. I'm attaching an image of the shapes of tags that I like, along with a copy of our logo. On the larger company tag I'd like our logo in the center and a color block stripe of the yellow color of our logo at the bottom, on the flip side there will just be text, sort of our company motto. On the narrower longer product info tag I'd like a small logo at the bottom end and space for product information to be written in by hand and on the flip side of this one lines for what country it's from, what community created it and care instructions, again, all information that we will write in by hand. Please let me know if you have questions.

Target Market(s)

Design savvy, house proud, well educated people who travel and appreciate art.

Font styles to use
Sans Serif

Requirements
Must have
• I want it to look graphic, sophisticated and modern. I want to be very legible and clean.
Nice to have
• Clarity, easy to read, and maybe a bit of whimsy or lightheartedness.
Should not have
• Nothing that feels "ethnic" or "crafty:, even though our products are handmade in Latin America they are contemporary and sophisticated, not stereotypical.

```html
<!DOCTYPE html>
<html lang="en">
<head>
<meta charset="utf-8">
<title>Verbena Home – Hang Tags</title>
<link href="https://fonts.googleapis.com/css2?family=Questrial&display=swap" rel="stylesheet">
<style>
  :root {
    --page: #ffffff;
    --yellow: #fccf0a;
    --band: #e0b515;
    --photo-dark-top: #5a4632;
    --photo-dark-bottom: #3f2c1e;
    --photo-light-top: #93795a;
    --photo-light-bottom: #7f6547;
    --text-light: #ffffff;
    --text-dark: #2a2216;
  }
  html, body {
    margin: 0;
    padding: 0;
    width: 1200px;
    height: 1200px;
    overflow: hidden;
    background: var(--page);
    font-family: "Questrial", sans-serif;
  }
  .canvas {
    position: relative;
    width: 1200px;
    height: 1200px;
  }
  .tag {
    position: absolute;
    top: 234px;
    width: 383px;
    height: 733px;
    overflow: hidden;
  }
  .tag--front {
    left: 87px;
    border-radius: 0 76px 0 76px;
  }
  .tag--back {
    left: 730px;
    border-radius: 76px 0 76px 0;
  }
  .tag__photo {
    position: absolute;
    inset: 0;
  }
  .tag--front .tag__photo {
    background: linear-gradient(170deg, var(--photo-dark-top) 0%, #6a4a36 45%, var(--photo-dark-bottom) 100%);
  }
  .tag--back .tag__photo {
    background: linear-gradient(170deg, var(--photo-light-top) 0%, #8a6d4e 50%, var(--photo-light-bottom) 100%);
  }
  .tag__band {
    position: absolute;
    left: 0;
    right: 0;
    bottom: 0;
    height: 72px;
    background: var(--band);
  }
  .tag__hole {
    position: absolute;
    top: 36px;
    width: 48px;
    height: 48px;
    border-radius: 50%;
    background: var(--page);
  }
  .tag--front .tag__hole { left: 301px; }
  .tag--back .tag__hole { left: 36px; }

  .brand-dot {
    position: absolute;
    border-radius: 50%;
    background: var(--yellow);
  }
  .tag--front .brand-dot {
    width: 100px;
    height: 100px;
    left: 141px;
    top: 190px;
  }
  .tag--back .brand-dot {
    width: 58px;
    height: 58px;
    left: 163px;
    top: 76px;
  }
  .brand-name {
    position: absolute;
    left: 0;
    right: 0;
    text-align: center;
    color: var(--text-light);
    margin: 0;
    font-weight: 400;
    line-height: 1;
  }
  .tag--front .brand-name {
    top: 352px;
    font-size: 68px;
  }
  .tag--back .brand-name {
    top: 146px;
    font-size: 32px;
  }
  .web {
    position: absolute;
    left: 0;
    right: 0;
    text-align: center;
    font-size: 16px;
    letter-spacing: 0.32em;
    margin: 0;
  }
  .tag--front .web {
    top: 424px;
    color: var(--text-light);
  }
  .tag--back .web {
    top: 686px;
    color: var(--text-dark);
  }
  .handmade-mark {
    position: absolute;
    left: 282px;
    top: 572px;
    width: 86px;
    height: 78px;
    border-radius: 10px;
    background: rgba(255, 255, 255, 0.18);
  }
  .motto {
    position: absolute;
    left: 40px;
    right: 40px;
    top: 226px;
    margin: 0;
    text-align: center;
    color: var(--text-light);
    font-size: 20px;
    line-height: 47px;
  }
</style>
</head>
<body>
<main class="canvas">
  <section class="tag tag--front">
    <div class="tag__photo" role="img" aria-label="Photo of a woven cord lounge chair in a warm interior with a branch wall decal"></div>
    <div class="tag__band"></div>
    <div class="tag__hole"></div>
    <div class="brand-dot"></div>
    <h1 class="brand-name">verbena</h1>
    <p class="web">www.verbenahome.com</p>
    <div class="handmade-mark" role="img" aria-label="Hand lettered 'Hand made' script mark"></div>
  </section>

  <section class="tag tag--back">
    <div class="tag__photo" role="img" aria-label="Faded photo of the woven cord chair interior behind a warm brown tint"></div>
    <div class="tag__band"></div>
    <div class="tag__hole"></div>
    <div class="brand-dot"></div>
    <h2 class="brand-name">verbena</h2>
    <p class="motto">Verbena Home is a home<br>décor studio co-creating<br>beautiful and unique<br>handmade pieces with<br>artisan partners throughout<br>Latin America, made by hand<br>and heart and designed for<br>the modern home.</p>
    <p class="web">www.verbenahome.com</p>
  </section>
</main>
</body>
</html>
```